Schulungen und Brandschutzdienstleistungen
Zielgruppe
Wir sind im vorbeugenden und organisatorischen Brandschutz tätig. Unsere Zielgruppe sind Firmen die Unterstützung, Beratung und die Schulung Ihrer Mitarbeiter beötigen.
Aufgabenstellung
Vorgaben ergeben sich aus dem Design der Homepage und dem pdf Upload (Beispiel des letzten Flyers).
Es sollen die Schulungsleistungen wie Brandschutzhelfer, Erste Hilfe und Unterweisungen hervorgehoben werden. Weiterhin sollen unsere Dienstleistungen, insbesondere der externe Brandschutzbeauftragte, aufgezeigt werden.
Schön währe auf der letzten Seite ein Anmeldeformular für die Schulungen.
Texte und Logo dürfen gerne verwendet werden.
Die Flyer soll zusammen mit einem Anschreiben in eine DIN lang Briefumschlag passen.

```html
<!DOCTYPE html>
<html lang="de">
<head>
<meta charset="utf-8">
<title>Brandschutz Kolbeck – Schulungen und Dienstleistungen</title>
<link href="https://fonts.googleapis.com/css2?family=Open+Sans:wght@600;700&family=Source+Sans+3:wght@400;600;700&display=swap" rel="stylesheet">
<style>
  :root {
    --red-dark: #8c0d14;
    --red-text: #9b1a1f;
    --white: #ffffff;
    --ink: #1f1f1f;
    --line: #3a3a3a;
  }
  * { margin: 0; padding: 0; box-sizing: border-box; }
  html, body { width: 1200px; height: 856px; overflow: hidden; background: #ffffff; }
  body { font-family: "Source Sans 3", Arial, sans-serif; color: var(--ink); }
  .heading { font-family: "Open Sans", Arial, sans-serif; }
  .flyer { position: relative; width: 1200px; height: 856px; overflow: hidden; }
  .panel { position: absolute; top: 0; height: 856px; overflow: hidden; }

  /* Left panel */
  .panel--first-aid { left: 0; width: 399px; background: var(--red-dark); }
  .photo--training {
    position: absolute; left: 0; top: 0; width: 399px; height: 452px;
    background: linear-gradient(160deg, #d9d6d2 0%, #b7b1aa 35%, #8e8a88 60%, #d9c3b2 100%);
    clip-path: polygon(0 0, 100% 0, 100% 92%, 0 100%);
  }
  .heading-band { position: absolute; left: 0; top: 0; width: 399px; height: 460px; }
  .first-aid__title {
    position: absolute; left: 18px; top: 362px;
    font-size: 30px; font-weight: 700; color: var(--red-text); letter-spacing: 0.2px;
  }
  .first-aid__text {
    position: absolute; left: 28px; top: 484px; width: 355px;
    color: var(--white); font-size: 15px; line-height: 19.5px;
    text-align: justify; hyphens: auto; -webkit-hyphens: auto;
  }
  .first-aid__text p + p { margin-top: 19px; }
  .notice {
    position: absolute; left: 9px; top: 674px; width: 367px; height: 126px;
    background: var(--white); box-shadow: 3px 3px 6px rgba(0,0,0,0.45);
    padding: 8px 10px; color: var(--red-text); font-weight: 700;
    font-size: 14.2px; line-height: 18.5px;
    text-align: justify; hyphens: auto; -webkit-hyphens: auto;
  }

  /* Middle panel */
  .panel--form { left: 399px; width: 389px; background: var(--white); box-shadow: inset 6px 0 8px -4px rgba(0,0,0,0.35); }
  .form__title {
    position: absolute; left: 23px; top: 18px;
    font-size: 27px; font-weight: 700; color: var(--red-text); letter-spacing: 0.3px;
  }
  .field { position: absolute; left: 23px; width: 351px; display: flex; align-items: flex-end; font-size: 15px; }
  .field__line { flex: 1; border-bottom: 1px solid var(--line); margin-left: 3px; height: 1px; margin-bottom: 3px; }
  .form__choice { position: absolute; left: 23px; top: 429px; color: var(--red-text); font-weight: 600; font-size: 15.5px; line-height: 26px; }
  .checkbox { position: absolute; top: 490px; display: flex; align-items: center; color: var(--red-text); font-weight: 600; font-size: 15.5px; }
  .checkbox__box { width: 19px; height: 19px; border: 1.5px solid var(--line); margin-right: 7px; }
  .date-field { position: absolute; left: 23px; top: 545px; display: flex; align-items: flex-end; color: var(--red-text); font-weight: 600; font-size: 15.5px; }
  .date-field__line { width: 143px; border-bottom: 1px solid var(--line); margin-left: 7px; margin-bottom: 3px; }
  .sign { position: absolute; top: 617px; border-top: 1px solid var(--line); text-align: center; font-size: 15.5px; padding-top: 3px; }
  .form__reach { position: absolute; left: 0; width: 389px; top: 662px; text-align: center; color: var(--red-text); font-weight: 700; font-size: 19px; }
  .contact-band { position: absolute; left: 0; top: 695px; width: 389px; height: 161px; background: var(--red-dark); color: var(--white); font-size: 12.5px; line-height: 17px; }
  .contact-col { position: absolute; top: 24px; text-align: center; }
  .contact-col--address { left: 8px; width: 192px; }
  .contact-col--web { left: 194px; width: 190px; }
  .contact-col strong { font-weight: 700; }
  .contact-col .gap { height: 13px; }

  /* Right panel */
  .panel--cover { left: 788px; width: 412px; background: var(--white); }
  .cover__head { position: absolute; left: 0; top: 0; width: 402px; height: 151px; background: var(--red-dark); }
  .cover__title { position: absolute; left: 17px; top: 14px; color: var(--white); font-weight: 700; font-size: 47px; line-height: 63px; letter-spacing: 0.5px; }
  .photo--extinguisher {
    position: absolute; left: 0; top: 151px; width: 412px; height: 637px;
    background: linear-gradient(135deg, #e8e6e3 0%, #c9c5c1 30%, #d44a3e 55%, #e2352a 75%, #b8201b 100%);
  }
  .ribbon {
    position: absolute; left: 22px; top: 505px; width: 410px; height: 96px;
    background: var(--red-dark); transform: rotate(-7deg); transform-origin: left top;
    box-shadow: 2px 3px 6px rgba(0,0,0,0.35);
    color: var(--white); font-weight: 700; font-size: 27px; line-height: 36px;
    text-align: center; padding-top: 12px; letter-spacing: 0.6px;
  }
  .cover__foot { position: absolute; left: 0; top: 788px; width: 412px; height: 68px; background: var(--red-dark); }
  .cover__year { position: absolute; left: 0; width: 412px; top: 776px; text-align: center; color: var(--white); font-weight: 700; font-size: 60px; line-height: 80px; }
</style>
</head>
<body>
<main class="flyer">

  <section class="panel panel--first-aid">
    <div class="photo photo--training" role="img" aria-label="Foto: Teilnehmer üben Herz-Lungen-Wiederbelebung an einer Übungspuppe"></div>
    <svg class="heading-band" viewBox="0 0 399 460" aria-hidden="true">
      <polygon points="0,352 399,346 399,405 0,446" fill="rgba(255,255,255,0.82)"/>
    </svg>
    <h2 class="first-aid__title heading">ERSTE-HILFE-KURSE:</h2>
    <div class="first-aid__text">
      <p>Lernen Sie in Notsituationen richtig handeln und helfen zu können und rüsten Sie sich für Notfälle im privaten und beruflichen Umfeld.</p>
      <p>Unsere anerkannten Fachdozenten sind alle seit Jahren im Rettungsdienst tätig und vermitteln auf spannender Weise Ihr umfangreiches Fachwissen mit praxisorientierten Fallbeispielen.</p>
    </div>
    <div class="notice">Als anerkannte und von den Berufsgenossenschaften ermächtigte Ausbildungsstelle für betriebliche Ersthelfer ist die Übernahme der Ausbildungskosten durch die BG bzw. Unfallversicherungsträger bei uns möglich!</div>
  </section>

  <section class="panel panel--form">
    <h2 class="form__title heading">ANMELDEFORMULAR:</h2>
    <div class="field" style="top:69px"><span>Firma:</span><span class="field__line"></span></div>
    <div class="field" style="top:115px"><span>Teilnehmer:</span><span class="field__line"></span></div>
    <div class="field" style="top:160px"><span>Name:</span><span class="field__line"></span></div>
    <div class="field" style="top:204px"><span>Vorname:</span><span class="field__line"></span></div>
    <div class="field" style="top:248px"><span>Straße:</span><span class="field__line"></span></div>
    <div class="field" style="top:296px"><span>PLZ, Wohnort:</span><span class="field__line"></span></div>
    <div class="field" style="top:340px"><span>Telefon:</span><span class="field__line"></span></div>
    <div class="field" style="top:385px"><span>E-Mail:</span><span class="field__line"></span></div>

    <p class="form__choice">Ich/Wir möchte/n an folgender<br>Schulung teilnehmen:</p>
    <div class="checkbox" style="left:23px"><span class="checkbox__box"></span>Brandschutzhelfer</div>
    <div class="checkbox" style="left:180px"><span class="checkbox__box"></span>Erste Hilfe</div>

    <div class="date-field">Gewünschter Termin:<span class="date-field__line"></span></div>
    <div class="sign" style="left:23px;width:130px">Datum</div>
    <div class="sign" style="left:193px;width:181px">Unterschrift</div>

    <h3 class="form__reach">So erreichen Sie uns:</h3>
    <div class="contact-band">
      <div class="contact-col contact-col--address">
        <strong>Brandschutz Kolbeck</strong><br>Lindenweg 7<br>12345 Musterstadt
        <div class="gap"></div>
        (01234) 5550123<br>info@brandschutz-kolbeck.de
      </div>
      <div class="contact-col contact-col--web">
        Besuchen Sie uns im Web:
        <div class="gap"></div>
        <strong>www.brandschutz-kolbeck.de</strong>
        <div class="gap"></div>
        Seminare und Schulungen<br>auch online buchbar.
      </div>
    </div>
  </section>

  <section class="panel panel--cover">
    <div class="photo photo--extinguisher" role="img" aria-label="Foto: roter Feuerlöscher auf einem Schild in einem Flur"></div>
    <div class="cover__head"><h1 class="cover__title heading">BRANDSCHUTZ<br>KOLBECK</h1></div>
    <div class="ribbon heading">SCHULUNGEN UND<br>DIENSTLEISTUNGEN</div>
    <div class="cover__foot"></div>
    <div class="cover__year heading">2017</div>
  </section>

</main>
</body>
</html>
```